LUMO - Óptica Clarena - web design and concept

Website concept - Create and develop our website design and structure. LUMO is an optical store chain, and we are looking to establish our web and digital concept. In attachment there are several pictures about our stores and our logo.

The website structure should be user friendly. Colors should be light and the design as simple and minimalist as possible. There are different variations of the logothat can be used, check the file.

The website will include optical collections and sun collections as an online store. Also, a medical menu should be considered in order for clients to schedule optometry appointments. There should also be a menu for client assistance where the clients can read about glass maintenance in our workshop.

Number of Pages Required

5+ page

Font styles to use
Serif
Sans Serif

Requirements
Must have
• Must be user-friendly and minimalist.
• Please USE PICTURES FROM THE BRANDS we sell: BRELO, MORVE, PKS, KOSU, NERAP
Nice to have
• Nice to inspire: ZEB glasses (see website https://ch.shopzeb-example.com/en/)
• Nice to inspire: https://brelo-eyewear-example.com/
• Nice to ispire: https://www.pksplanet-example.com/en/
Should not have
• Hysteric colors and shapes

```html
<!DOCTYPE html>
<html lang="en">
<head>
<meta charset="utf-8">
<title>LUMO – Óptica Clarena</title>
<link href="https://fonts.googleapis.com/css2?family=Open+Sans:wght@400;600;700&display=swap" rel="stylesheet">
<style>
  :root {
    --ink: #222222;
    --muted: #8a8a8a;
    --line: #e4e4e4;
    --panel: #f5f5f5;
    --card: #f4f4f4;
    --footer: #f2f2f2;
    --bottom: #ebebeb;
    --white: #ffffff;
  }
  * { box-sizing: border-box; margin: 0; padding: 0; }
  html, body { width: 1200px; height: 2416px; overflow: hidden; }
  body { font-family: "Open Sans", Arial, sans-serif; color: var(--ink); background: var(--white); position: relative; }
  .abs { position: absolute; }

  .site-nav { top: 0; left: 0; width: 1200px; height: 48px; background: var(--white); display: flex; align-items: center; justify-content: center; }
  .nav-menu { display: flex; gap: 34px; font-size: 11px; font-weight: 600; list-style: none; }
  .nav-menu li::after { content: " ▾"; font-size: 8px; color: var(--muted); }
  .nav-menu li:first-child::after { content: ""; }
  .nav-tools { position: absolute; right: 40px; top: 16px; display: flex; gap: 22px; }

  .hero { top: 48px; left: 0; width: 1200px; height: 340px;
    background: linear-gradient(180deg, #1a1d20 0%, #2e3a3c 30%, #6f8a86 48%, #a89b7c 62%, #c9c2b4 80%, #e3ded6 100%); }

  .featured-frame { top: 448px; width: 200px; height: 72px; }
  .frame-clear { background: linear-gradient(180deg, #f7f7f7 0%, #e6e6e6 50%, #f7f7f7 100%); }
  .frame-tinted { background: linear-gradient(180deg, #eef1f3 0%, #b9c4cc 50%, #eef1f3 100%); }

  .category { width: 600px; height: 396px; }
  .category-panel { background: var(--panel); display: flex; flex-direction: column; align-items: center; justify-content: center; }
  .category-title { font-size: 15px; font-weight: 700; }
  .category-link { margin-top: 22px; font-size: 9px; color: var(--muted); border-bottom: 1px solid var(--muted); padding-bottom: 1px; }
  .photo-women { background: linear-gradient(160deg, #c9c7c2 0%, #8d8b86 40%, #3e3d39 70%, #8a8983 100%); }
  .photo-men { background: linear-gradient(180deg, #3a4252 0%, #5b6676 40%, #7e8894 70%, #4a4f58 100%); }

  .section-title { top: 1428px; left: 0; width: 1200px; text-align: center; font-size: 15px; font-weight: 700; }
  .section-rule { top: 1456px; left: 585px; width: 30px; height: 2px; background: var(--ink); }

  .product { width: 232px; text-align: center; }
  .product-image { width: 232px; height: 150px; }
  .tone-brown { background: radial-gradient(ellipse 45% 22% at 50% 50%, #c8a27c 0%, #ead9c8 60%, var(--card) 100%); }
  .tone-rose { background: radial-gradient(ellipse 45% 22% at 50% 50%, #c6aea6 0%, #e8dcd8 60%, var(--card) 100%); }
  .tone-grey { background: radial-gradient(ellipse 45% 22% at 50% 50%, #8e8e8e 0%, #d8d8d8 60%, var(--card) 100%); }
  .tone-dark { background: radial-gradient(ellipse 45% 22% at 50% 50%, #5a5a5a 0%, #cfcfcf 60%, var(--card) 100%); }
  .tone-black { background: radial-gradient(ellipse 45% 22% at 50% 50%, #333333 0%, #c9c9c9 60%, var(--card) 100%); }
  .tone-blue { background: radial-gradient(ellipse 45% 22% at 50% 50%, #4e6272 0%, #c8cfd5 60%, var(--card) 100%); }
  .product-name { margin-top: 12px; font-size: 11px; font-weight: 700; }
  .product-price { margin-top: 3px; font-size: 9px; color: var(--muted); }

  .divider { top: 1912px; left: 0; width: 1200px; height: 1px; background: var(--line); }
  .instagram-title { top: 2010px; left: 240px; font-size: 15px; font-weight: 700; }
  .instagram-handle { top: 2034px; left: 240px; font-size: 9px; color: var(--muted); }
  .insta-tile { top: 1960px; width: 168px; height: 168px; }
  .tile-a { background: linear-gradient(135deg, #a7b8b9 0%, #c89a7a 55%, #7d5b45 100%); }
  .tile-b { background: linear-gradient(135deg, #f0a69a 0%, #f0a69a 50%, #4aa7c9 50%, #3e9fc4 100%); }
  .tile-c { background: linear-gradient(160deg, #5d7a55 0%, #3a4d35 50%, #2a2a28 100%); }

  .site-footer { top: 2192px; left: 0; width: 1200px; height: 188px; background: var(--footer); }
  .footer-col { top: 2226px; width: 170px; font-size: 9px; color: var(--muted); line-height: 1.85; }
  .footer-col h4 { font-size: 11px; font-weight: 700; color: var(--ink); margin-bottom: 10px; }
  .newsletter-button { display: inline-block; margin-top: 10px; border-bottom: 1px solid var(--muted); color: var(--ink); }
  .bottom-bar { top: 2380px; left: 0; width: 1200px; height: 36px; background: var(--bottom); font-size: 8px; color: var(--muted); padding: 13px 240px; }
</style>
</head>
<body>

<header class="site-nav abs">
  <ul class="nav-menu">
    <li>Home</li><li>About Us</li><li>Services</li><li>News</li><li>Pages</li><li>Shop</li>
  </ul>
  <div class="nav-tools">
    <svg width="14" height="14" viewBox="0 0 14 14"><circle cx="6" cy="6" r="4.5" fill="none" stroke="#222" stroke-width="1.5"/><line x1="9.3" y1="9.3" x2="13" y2="13" stroke="#222" stroke-width="1.5"/></svg>
    <svg width="14" height="14" viewBox="0 0 14 14"><path d="M2 4h10l-1 9H3z" fill="none" stroke="#222" stroke-width="1.4"/><path d="M5 4V3a2 2 0 0 1 4 0v1" fill="none" stroke="#222" stroke-width="1.4"/></svg>
  </div>
</header>

<div class="hero abs" role="img" aria-label="Interior of a LUMO eyewear store with illuminated display walls"></div>

<div class="featured-frame frame-clear abs" style="left:312px" role="img" aria-label="Product photo: black round optical frame"></div>
<div class="featured-frame frame-tinted abs" style="left:684px" role="img" aria-label="Product photo: black sunglasses with blue tinted lenses"></div>

<section class="category category-panel abs" style="top:596px;left:0">
  <h3 class="category-title">Women's Sunglasses</h3>
  <span class="category-link">Shop Now</span>
</section>
<div class="category photo-women abs" style="top:596px;left:600px" role="img" aria-label="Woman in a hat and dark coat wearing sunglasses on a city street"></div>
<div class="category photo-men abs" style="top:992px;left:0" role="img" aria-label="Sneakers on a stone step with round optical glasses on the ground"></div>
<section class="category category-panel abs" style="top:992px;left:600px">
  <h3 class="category-title">Men's Optics</h3>
  <span class="category-link">Shop Now</span>
</section>

<h2 class="section-title abs">Men's Sunglasses</h2>
<div class="section-rule abs"></div>

<article class="product abs" style="top:1480px;left:240px">
  <div class="product-image tone-brown" role="img" aria-label="Product photo: aviator sunglasses with brown lenses"></div>
  <h4 class="product-name">Alpha Sunglasses</h4><p class="product-price">$120.00</p>
</article>
<article class="product abs" style="top:1480px;left:484px">
  <div class="product-image tone-rose" role="img" aria-label="Product photo: aviator sunglasses with rose lenses"></div>
  <h4 class="product-name">Bravo Sunglasses</h4><p class="product-price">$135.00</p>
</article>
<article class="product abs" style="top:1480px;left:728px">
  <div class="product-image tone-grey" role="img" aria-label="Product photo: aviator sunglasses with grey lenses"></div>
  <h4 class="product-name">Charlie Sunglasses</h4><p class="product-price">$110.00</p>
</article>
<article class="product abs" style="top:1688px;left:240px">
  <div class="product-image tone-dark" role="img" aria-label="Product photo: round sunglasses with dark lenses"></div>
  <h4 class="product-name">Delta Sunglasses</h4><p class="product-price">$95.00</p>
</article>
<article class="product abs" style="top:1688px;left:484px">
  <div class="product-image tone-black" role="img" aria-label="Product photo: black frame sunglasses with dark lenses"></div>
  <h4 class="product-name">Foxtrot Sunglasses</h4><p class="product-price">$150.00</p>
</article>
<article class="product abs" style="top:1688px;left:728px">
  <div class="product-image tone-blue" role="img" aria-label="Product photo: black frame sunglasses with blue lenses"></div>
  <h4 class="product-name">Golo Sunglasses</h4><p class="product-price">$140.00</p>
</article>

<div class="divider abs"></div>
<h2 class="instagram-title abs">Instagram</h2>
<p class="instagram-handle abs">@lumo_clarena</p>
<div class="insta-tile tile-a abs" style="left:424px" role="img" aria-label="Couple outdoors wearing sunglasses"></div>
<div class="insta-tile tile-b abs" style="left:608px" role="img" aria-label="Round sunglasses on a pink and blue background"></div>
<div class="insta-tile tile-c abs" style="left:792px" role="img" aria-label="Woman in sunglasses among green leaves"></div>

<footer class="site-footer abs"></footer>
<div class="footer-col abs" style="left:240px"><h4>London</h4>12 Harbour Lane<br>Westfield Quarter<br>London EC2 4LP<br>Mon–Sat 9–19</div>
<div class="footer-col abs" style="left:424px"><h4>New York</h4>85 Mercer Street<br>SoHo District<br>New York NY<br>Mon–Sat 9–19</div>
<div class="footer-col abs" style="left:608px"><h4>Toronto</h4>40 King Street<br>Old Town<br>Toronto ON M5<br>Mon–Sat 9–19</div>
<div class="footer-col abs" style="left:792px"><h4>Newsletter</h4>Sign up for news and offers<br><span class="newsletter-button">Subscribe</span></div>
<div class="bottom-bar abs">© 2024 LUMO Óptica Clarena. All rights reserved.</div>

</body>
</html>
```